New Business Card Design For Re-Branded Company (New Logo)

We recently switched our DBA and had a new logo designed. We now need new business cards made around our new logo. We would like to stick with the color scheme in our logo: White, Orange, and Blue. We want to see original bold designs that reflect our position in the solar energy sector but we prefer simple over complicated.

We are curious about vertical designs so if you can translate your design onto a vertical layout we would be open to look at it. We especially like a few designs we have seen on here that are vertical with a black or very dark gray background. They have our logo on one side and then the normal vertical business card on the other side.

I have included a screenshot of one of the samples we like, labeled sample.jpg and a file we were given as an example of our logo on a dark background.

At the same time we are satisfied to stay with what we have always had in a horizontal format. If it's not a lot of extra work for you, designs that are submitted in both horizontal and vertical formats will be greatly appreciated.

Please submit your original, bold, clean designs for consideration. Contact us with any questions or comments that may arise.

Thank you and Good Luck,

RT

```html
<!DOCTYPE html>
<html lang="en">
<head>
<meta charset="utf-8">
<title>Brightfield Solar – Business Card</title>
<link href="https://fonts.googleapis.com/css2?family=Lato:wght@400;700;900&display=swap" rel="stylesheet">
<style>
  :root {
    --stage: #2b2b2d;
    --blue: #1a73b8;
    --blue-deep: #0f5f9e;
    --orange: #e8742a;
    --white: #ffffff;
    --ink-soft: #dfe9f3;
    --icon-tile: #e9b48c;
  }
  * { box-sizing: border-box; margin: 0; padding: 0; }
  html, body {
    width: 1200px; height: 997px; overflow: hidden;
    background: var(--stage);
    font-family: "Lato", Arial, sans-serif;
  }
  .stage {
    width: 1200px; height: 997px;
    display: flex; align-items: center; justify-content: center; gap: 90px;
  }
  .card {
    width: 390px; height: 640px;
    border-radius: 30px;
    overflow: hidden;
    position: relative;
    box-shadow: 0 18px 40px rgba(0,0,0,.45);
  }
  /* back side */
  .card-back {
    background: linear-gradient(160deg, var(--blue) 0%, var(--blue-deep) 100%);
    display: flex; align-items: center; justify-content: center;
  }
  .brand {
    display: flex; align-items: center; gap: 12px;
    font-weight: 700; letter-spacing: .5px;
  }
  .brand-mark {
    width: 26px; height: 26px; border-radius: 50%;
    background: var(--orange); flex: none;
  }
  .card-back .brand { color: var(--white); font-size: 30px; }
  /* front side */
  .card-front { background: linear-gradient(175deg, var(--blue) 0%, var(--blue-deep) 100%); }
  .front-header {
    height: 215px; background: var(--white);
    display: flex; align-items: center; justify-content: center;
  }
  .card-front .brand { color: var(--blue); font-size: 30px; }
  .person {
    padding: 58px 0 0 44px; color: var(--white);
  }
  .person-name { font-weight: 700; font-size: 26px; letter-spacing: .5px; }
  .person-role { font-size: 17px; color: var(--ink-soft); margin-top: 4px; }
  .contacts {
    position: absolute; left: 56px; bottom: 58px;
    list-style: none; color: var(--ink-soft); font-size: 20px;
  }
  .contacts li { display: flex; align-items: center; gap: 18px; margin-top: 16px; }
  .contact-icon {
    width: 26px; height: 26px; background: var(--icon-tile);
    display: flex; align-items: center; justify-content: center; flex: none;
  }
</style>
</head>
<body>
<main class="stage">
  <section class="card card-back" aria-label="Card back">
    <div class="brand"><span class="brand-mark"></span><span>BRIGHTFIELD SOLAR</span></div>
  </section>

  <section class="card card-front" aria-label="Card front">
    <header class="front-header">
      <div class="brand"><span class="brand-mark"></span><span>BRIGHTFIELD SOLAR</span></div>
    </header>
    <div class="person">
      <p class="person-name">DANIEL MARSH</p>
      <p class="person-role">Principal - Financial Planner</p>
    </div>
    <ul class="contacts">
      <li>
        <span class="contact-icon">
          <svg width="14" height="18" viewBox="0 0 14 18"><rect x="1.5" y="1" width="11" height="16" rx="2" fill="none" stroke="#c0521a" stroke-width="2"/></svg>
        </span>
        <span>0400 123 456</span>
      </li>
      <li>
        <span class="contact-icon">
          <svg width="18" height="14" viewBox="0 0 18 14"><rect x="1" y="1" width="16" height="12" fill="none" stroke="#c0521a" stroke-width="1.8"/><path d="M1 1 L9 8 L17 1" fill="none" stroke="#c0521a" stroke-width="1.8"/></svg>
        </span>
        <span>dan@norvale.com.au</span>
      </li>
      <li>
        <span class="contact-icon">
          <svg width="18" height="18" viewBox="0 0 18 18"><circle cx="9" cy="9" r="7.5" fill="none" stroke="#c0521a" stroke-width="1.6"/><ellipse cx="9" cy="9" rx="3.2" ry="7.5" fill="none" stroke="#c0521a" stroke-width="1.4"/><path d="M1.5 9 H16.5" stroke="#c0521a" stroke-width="1.4"/></svg>
        </span>
        <span>www.norvale.au</span>
      </li>
    </ul>
  </section>
</main>
</body>
</html>
```